Email Banner - TamberFold.com

I need an email banner created for my website: Tamberfold.com.
The logos are attatched here and an example of an email banner we have used in the past is also attatched. Please keep the tagline: "Essential Whitepapers for Business Professionals" - The logos are in the marvotta zip folder.

Logo Text

Tamberfold

```html
<!DOCTYPE html>
<html lang="en">
<head>
<meta charset="UTF-8">
<title>Tamberfold – Email Banner</title>
<link rel="stylesheet" href="https://fonts.googleapis.com/css2?family=Figtree:wght@400;500;700;800&display=swap">
<style>
  :root {
    --canvas-bg: #cbcbcb;
    --banner-navy: #243083;
    --cloud-white: #ffffff;
    --brand-ink: #243a94;
    --cta-blue: #3a6ff5;
    --text-light: #ffffff;
  }
  * { margin: 0; padding: 0; box-sizing: border-box; }
  html, body {
    width: 1200px;
    height: 1200px;
    overflow: hidden;
    background: var(--canvas-bg);
    font-family: "Figtree", Arial, sans-serif;
  }
  .email-banner {
    position: absolute;
    left: 178px;
    top: 533px;
    width: 844px;
    height: 134px;
    background: var(--banner-navy);
    overflow: hidden;
  }
  .cloud-shape {
    position: absolute;
    left: 0;
    top: 0;
    width: 844px;
    height: 134px;
  }
  .brand-name {
    position: absolute;
    left: 44px;
    top: 74px;
    width: 212px;
    text-align: center;
    font-size: 30px;
    font-weight: 700;
    letter-spacing: -0.4px;
    color: var(--brand-ink);
    line-height: 1;
  }
  .tagline {
    position: absolute;
    left: 367px;
    top: 34px;
    color: var(--text-light);
    font-size: 22.5px;
    font-weight: 400;
    line-height: 31px;
  }
  .tagline strong { font-weight: 700; }
  .cta-button {
    position: absolute;
    right: 0;
    top: 0;
    width: 148px;
    height: 40px;
    background: var(--cta-blue);
    border-bottom-left-radius: 14px;
    color: var(--text-light);
    font-size: 16px;
    font-weight: 800;
    letter-spacing: 0.2px;
    display: flex;
    align-items: center;
    justify-content: center;
    text-decoration: none;
  }
</style>
</head>
<body>
  <div class="email-banner">
    <svg class="cloud-shape" viewBox="0 0 720 114" aria-hidden="true">
      <g fill="var(--cloud-white)">
        <circle cx="90" cy="50" r="52"/>
        <circle cx="190" cy="68" r="62"/>
        <circle cx="245" cy="112" r="53"/>
        <circle cx="40" cy="118" r="55"/>
        <rect x="0" y="80" width="250" height="34"/>
        <rect x="60" y="60" width="150" height="54"/>
      </g>
    </svg>
    <div class="brand-name">Tamberfold</div>
    <p class="tagline">Essential Whitepapers<br>for <strong>Business Professionals</strong></p>
    <a class="cta-button" href="#">CLICK HERE</a>
  </div>
</body>
</html>
```